Quillon Media - Amazing Homepage

We would like to build an amazing homepage for our site. We will need it built in HTM5, so it works across devices and would like it to parallax scroll , so it looks amazing.
We are a digital media agency, that has recently launched. Our old site is self build through one of the standard web build sites. We will be hosting our new site independently.
This is our old site - www.quillon-media.com
The new site only really needs one scrolling page to explain what we do and have our contact details at the bottom.
We have a place to host it, once designed. So we can share with the final design for you to upload.
Attached are:
Brief
Logos and artwork
Our PowerPoint template to give you an idea of colours

```html
<!DOCTYPE html>
<html lang="en">
<head>
<meta charset="utf-8">
<title>Quillon Media – Homepage</title>
<link rel="stylesheet" href="https://fonts.googleapis.com/css2?family=Lato:wght@300;400;700&family=Open+Sans:wght@300;400;600;700&family=Oswald:wght@600&display=swap">
<style>
:root{
  --maroon:#8b1a36;
  --ink:#333333;
  --muted:#666666;
  --pale:#b9b9b9;
  --contact-grey:#6d6d6d;
  --footer:#2b2b2b;
  --white:#ffffff;
}
*{margin:0;padding:0;box-sizing:border-box}
html,body{width:1200px;height:4986px;overflow:hidden}
body{font-family:"Open Sans",Arial,sans-serif;color:var(--ink);background:var(--white);position:relative}
section,header,footer{position:absolute;left:0;width:1200px}
.center{text-align:center}

/* header */
.site-header{top:0;height:123px;background:var(--white);border-bottom:4px solid var(--maroon)}
.brand{position:absolute;left:100px;top:40px;display:flex;align-items:center;gap:12px}
.brand-mark{width:14px;height:14px;background:var(--maroon)}
.brand-name{font-family:"Open Sans",sans-serif;font-weight:600;font-size:24px;color:var(--ink);line-height:1}
.main-nav{position:absolute;right:90px;top:40px;display:flex;gap:30px;align-items:center}
.main-nav a{font-size:16px;color:var(--ink);text-decoration:none;padding:14px 0}
.main-nav a.active{background:var(--maroon);color:var(--white);padding:14px 30px;border-radius:3px}

/* hero */
.hero{top:123px;height:534px;background:linear-gradient(180deg,#7a8aa3 0%,#41506a 40%,#202a3c 75%,#151b27 100%)}
.hero-title{position:absolute;top:178px;width:100%;font-family:"Oswald",sans-serif;font-weight:600;font-size:37px;color:var(--white);text-transform:uppercase;letter-spacing:.5px}
.hero-text{position:absolute;top:240px;left:150px;width:900px;font-size:14px;line-height:1.5;color:#e6e6e6}
.hero-btn{position:absolute;top:332px;left:525px;width:150px;height:56px;background:var(--maroon);color:var(--white);font-size:15px;line-height:56px;border-radius:3px;text-align:center;text-decoration:none}
.slider-dots{position:absolute;top:500px;left:0;width:100%;display:flex;justify-content:center;gap:10px}
.slider-dots span{width:9px;height:9px;border-radius:50%;background:rgba(255,255,255,.5)}
.slider-dots span:first-child{background:var(--white)}

/* welcome */
.welcome{top:657px;height:240px}
.welcome h2{margin-top:48px;font-family:"Lato",sans-serif;font-weight:400;font-size:32px;color:var(--maroon);letter-spacing:1px}
.welcome p{width:1110px;margin:14px auto 0;font-size:13px;line-height:1.65;color:var(--muted)}

/* clarity */
.clarity{top:897px;height:880px;background:linear-gradient(90deg,#eeeae4 0%,#f8f7f5 40%,#ffffff 65%,#f5f3ef 100%)}
.clarity-photo{position:absolute;left:0;top:0;width:370px;height:880px;background:linear-gradient(180deg,#d6c7b6 0%,#d3b190 40%,#c5705a 65%,#d0b27c 100%)}
.clarity-field{position:absolute;left:370px;bottom:0;width:830px;height:110px;background:linear-gradient(180deg,rgba(214,190,140,0) 0%,#d8c28f 100%)}
.clarity-copy{position:absolute;left:330px;top:250px;width:570px;text-align:center}
.clarity-copy h2{font-family:"Lato",sans-serif;font-weight:300;font-size:31px;line-height:1.3;color:var(--ink);text-transform:uppercase}
.clarity-copy p{margin-top:32px;font-size:16px;line-height:1.6;color:var(--ink)}
.clarity-copy strong{display:block;margin-top:22px;font-weight:700}

.chevron{position:absolute;left:580px;width:40px;height:40px;z-index:3}

/* statement */
.statement{top:1777px;height:258px;background:linear-gradient(180deg,#e4e4e4,#d2d2d2)}
.statement p{margin-top:52px;font-weight:400;font-size:36px;line-height:1.4;color:var(--maroon)}

/* coup */
.coup{top:2035px;height:803px;background:linear-gradient(135deg,#8c8c8c 0%,#6e6e6e 50%,#5a5a5a 100%)}
.coup-photo{position:absolute;left:135px;top:60px;width:500px;height:660px;background:linear-gradient(160deg,#e8d23a 0%,#d8bd22 60%,#9e8a1c 100%);border-radius:14px;opacity:.9}
.coup-copy{position:absolute;right:50px;top:80px;width:560px;text-align:right;font-weight:300;font-size:37px;line-height:1.3;color:var(--white)}

/* quiet coup */
.quiet{top:2838px;height:183px;background:var(--maroon)}
.quiet p{margin-top:45px;font-weight:400;font-size:64px;color:var(--white)}

/* growth */
.growth{top:3021px;height:614px;background:var(--white)}
.growth-graphic{position:absolute;left:465px;top:67px;width:270px;height:200px;background:linear-gradient(45deg,#cdd4e6 0%,#a9c4e2 45%,#8fc45a 100%);border-radius:6px}
.growth h3{position:absolute;top:318px;width:100%;font-weight:600;font-size:24px;line-height:1.35;color:var(--ink)}
.growth .lede{position:absolute;top:400px;width:100%;font-size:14px;color:var(--ink)}
.services{position:absolute;top:460px;width:100%;display:flex;justify-content:center;gap:32px;font-size:25px;color:var(--maroon);text-transform:uppercase}
.board{position:absolute;top:510px;width:100%;font-weight:300;font-size:32px;color:var(--pale);text-transform:uppercase}

/* results */
.results{top:3635px;height:797px;background:radial-gradient(ellipse at 50% 45%,#ffffff 0%,#ececec 55%,#d6d6d6 100%)}
.results-lead{position:absolute;top:92px;width:100%;font-size:34px;line-height:1.4;color:#555}
.results-heading{position:absolute;top:262px;width:100%;font-weight:700;font-size:50px;color:var(--white);letter-spacing:1px}
.results-brand{position:absolute;top:390px;width:100%;display:flex;justify-content:center;align-items:center;gap:18px}
.results-brand .brand-mark{width:34px;height:34px;background:#444}
.results-brand .brand-name{font-size:56px;color:#444}
.clients-label{position:absolute;top:628px;width:100%;font-size:13px;font-weight:700;letter-spacing:1px;color:#444;text-transform:uppercase}
.clients{position:absolute;top:678px;left:150px;width:900px;display:flex;justify-content:space-between;align-items:center}
.clients span{display:flex;align-items:center;gap:8px;font-weight:700;font-size:24px;color:#555}
.clients i{display:block;width:22px;height:22px;border-radius:50%;background:var(--maroon)}

/* contact */
.contact{top:4432px;height:332px;background:var(--contact-grey);color:var(--white)}
.contact p{margin-top:58px;font-size:34px;line-height:1.35}
.contact address{margin-top:20px;font-style:normal;font-weight:700;font-size:26px;line-height:1.6}

/* footer */
.site-footer{top:4764px;height:222px;background:var(--footer);color:#cfcfcf}
.footer-nav{margin-top:38px;display:flex;justify-content:center;gap:14px;font-size:12px;text-transform:uppercase}
.footer-nav a{color:#cfcfcf;text-decoration:none}
.footer-nav em{font-style:normal;color:#888}
.social{margin-top:34px;display:flex;justify-content:center;gap:14px}
.social span{width:42px;height:42px;border-radius:50%;background:#cfcfcf}
.copyright{margin-top:30px;font-size:11px;letter-spacing:.5px;color:#999}
</style>
</head>
<body>

<header class="site-header">
  <div class="brand">
    <span class="brand-mark"></span>
    <span class="brand-name">Quillon Media</span>
  </div>
  <nav class="main-nav">
    <a class="active" href="#">Home</a>
    <a href="#">About</a>
    <a href="#">What We Can Offer</a>
    <a href="#">Contact</a>
  </nav>
</header>

<section class="hero" role="img" aria-label="Night-time city skyline with towers lit up">
  <h1 class="hero-title center">Got the feeling your digital marketing just isn't quite 'there'?</h1>
  <p class="hero-text center">Lorem ipsum dolor sit amet, consectetuer adipiscing elit, sed diam nonummy nibh euismod tincidunt ut laoreet dolore magna aliquam erat volutpat. Ut wisi enim ad minim veniam, quis nostrud exerci tation ullamcorper suscipit lobortis.</p>
  <a class="hero-btn" href="#">Learn more</a>
  <div class="slider-dots"><span></span><span></span><span></span></div>
</section>

<section class="welcome center">
  <h2>WELCOME TO QUILLON</h2>
  <p>Lorem ipsum dolor sit amet, consectetuer adipiscing elit, sed diam nonummy nibh euismod tincidunt ut laoreet dolore magna aliquam erat volutpat. Ut wisi enim ad minim veniam, quis nostrud exerci tation ullamcorper suscipit lobortis nisl ut aliquip ex ea commodo consequat. Duis autem vel. Lorem ipsum dolor sit amet, consectetuer adipiscing elit, sed diam nonummy nibh euismod tincidunt ut laoreet dolore magna aliquam erat volutpat.</p>
</section>

<section class="clarity">
  <div class="clarity-photo" role="img" aria-label="Woman in a red top raising her arm in a sunlit field"></div>
  <div class="clarity-field"></div>
  <div class="clarity-copy">
    <h2>We keep fighting to give you<br>clarity by:</h2>
    <p>Creating a singular view ofyour digital eco system<br>
    Reviewing how and why your money is being spent where it is<br>
    Profiling your customers. Who doesn't have 1000's of different customers<br>with different motivations, interests and value to the brand?<br>
    Finding the best digital channels to communicate with them
    <strong>Because everything is changing every day…exciting isn't it!<br>Never stop, never settle, always improve. Be amazing.</strong></p>
  </div>
</section>

<svg class="chevron" style="top:1757px" viewBox="0 0 40 40" aria-hidden="true"><circle cx="20" cy="20" r="19" fill="#777"/><path d="M12 16l8 8 8-8" fill="none" stroke="#fff" stroke-width="3"/></svg>

<section class="statement center">
  <p>Every client deserves amazing work,<br>regardless of the brand, to big, small or new on the<br>scene you deserve amazing work</p>
</section>

<section class="coup">
  <div class="coup-photo" role="img" aria-label="Yellow wooden go-kart with black stripes on tarmac"></div>
  <p class="coup-copy">It's time to start a<br>coup…there are too many<br>large agency networks, too<br>few agencies being<br>transparent, too many<br>putting quality of work<br>second to income</p>
</section>

<svg class="chevron" style="top:2818px" viewBox="0 0 40 40" aria-hidden="true"><circle cx="20" cy="20" r="19" fill="#999"/><path d="M12 16l8 8 8-8" fill="none" stroke="#fff" stroke-width="3"/></svg>

<section class="quiet center">
  <p>Well, a very quiet coup.</p>
</section>

<section class="growth center">
  <div class="growth-graphic" role="img" aria-label="Colourful social media icons forming a rising growth arrow"></div>
  <h3>We've yet to come across a client that wants to shrink…<br>making us specialists in delivering growth!</h3>
  <p class="lede">We've been optimising our digital knowledge for over 20 years and &nbsp;we genuinely know what we are talking about</p>
  <div class="services"><span>PPC</span><span>SEO</span><span>Display</span><span>Paid Social</span><span>Data Management</span><span>Attribution</span></div>
  <p class="board">Operating at board level in top 10 digital agencies</p>
</section>

<section class="results center">
  <p class="results-lead">Happily, we smash it for all our clients,<br>with an average of 35% improvement in performance<br>within the first quarter of working with us</p>
  <h2 class="results-heading">WE MAKE AMAZING</h2>
  <div class="results-brand">
    <span class="brand-mark"></span>
    <span class="brand-name">Quillon Media</span>
  </div>
  <p class="clients-label">Logos of clients</p>
  <div class="clients">
    <span><i></i>Birchwell</span>
    <span>Calmora</span>
    <span>Velvra</span>
    <span>Stagepass</span>
    <span>Nestow</span>
  </div>
</section>

<section class="contact center">
  <p>If you are still reading our rant then<br>get in touch / follow us / let's go for a coffee</p>
  <address>Our address is : &nbsp;14 Harlow Court, London, EC2 9ZZ<br>Contact@quillon-media.com</address>
</section>

<footer class="site-footer center">
  <nav class="footer-nav">
    <a href="#">Home</a><em>/</em><a href="#">Who we are</a><em>/</em><a href="#">What we do</a><em>/</em><a href="#">What we can offer</a><em>/</em><a href="#">Clients</a><em>/</em><a href="#">Contact</a>
  </nav>
  <div class="social"><span></span><span></span><span></span><span></span><span></span><span></span></div>
  <p class="copyright">COPYRIGHT © 2014 QUILLON MEDIA. &nbsp;ALL RIGHTS RESERVED.</p>
</footer>

</body>
</html>
```